Tallowmere Capital Partners- Business Card

We need a professional business card that conveys confidence and trust. Strength. A modern and still yet, traditional financial planner/advisor format. I will upload a logo file or two, you do not have to use it, if it does not work for the design.

Target Market(s)

high net worth

Industry/Entity Type

Finance

Contact Information for Business Card

Address: 24836 Orchard Ave. Suite 400, Huntington Beach, CA 93518, website: tallowmerecap.example, ph # (555) 271-6094, email address: rpoulsen@tallowmerecap.example

```html
<!DOCTYPE html>
<html lang="en">
<head>
<meta charset="utf-8">
<title>Tallowmere Capital Partners – Business Card</title>
<link rel="stylesheet" href="https://fonts.googleapis.com/css2?family=Cormorant+Garamond:wght@600&family=Roboto:wght@400;700&display=swap">
<style>
  :root {
    --backdrop: #d3d6d7;
    --paper: #f7f7f6;
    --navy: #1d2760;
    --navy-deep: #161f52;
    --gold: #b58a2e;
    --ink: #3a3d45;
    --white: #ffffff;
  }
  * { box-sizing: border-box; margin: 0; padding: 0; }
  html, body { width: 1200px; height: 829px; overflow: hidden; }
  body {
    background: var(--backdrop);
    display: flex;
    align-items: center;
    justify-content: center;
    gap: 40px;
    font-family: "Roboto", Arial, sans-serif;
  }
  .card {
    width: 540px;
    height: 309px;
    position: relative;
    overflow: hidden;
    box-shadow: 0 10px 30px rgba(0,0,0,.18);
    border-bottom: 3px solid var(--gold);
  }
  .brand {
    display: flex;
    align-items: center;
    gap: 12px;
    font-family: "Cormorant Garamond", Georgia, serif;
    font-weight: 600;
    font-variant: small-caps;
    letter-spacing: .04em;
    white-space: nowrap;
  }
  .brand-mark { flex: none; border: 2px solid var(--gold); }

  /* Front */
  .card-front { background: var(--paper); }
  .card-front .brand {
    position: absolute; left: 96px; top: 34px;
    color: var(--navy); font-size: 23px;
  }
  .card-front .brand-mark { width: 24px; height: 24px; }
  .person {
    position: absolute; left: 36px; top: 104px; width: 160px;
    text-align: right;
  }
  .person-name {
    color: var(--navy); font-weight: 700; font-size: 21px;
    text-transform: uppercase; letter-spacing: -.01em;
  }
  .person-title { color: var(--ink); font-size: 12px; margin-top: 2px; }
  .divider {
    position: absolute; left: 212px; top: 104px;
    width: 1px; height: 66px; background: var(--gold); opacity: .6;
  }
  .contacts {
    position: absolute; left: 228px; top: 104px;
    list-style: none; color: var(--ink); font-size: 12.5px;
  }
  .contacts li { display: flex; align-items: center; gap: 8px; height: 22px; white-space: nowrap; }
  .contacts svg { width: 11px; height: 11px; fill: var(--gold); flex: none; }
  .address-band {
    position: absolute; left: 0; right: 0; top: 206px; height: 34px;
    background: var(--navy);
    color: var(--white); font-size: 13px;
    display: flex; align-items: center; padding-left: 36px;
  }

  /* Back */
  .card-back {
    background: var(--navy-deep);
    display: flex; align-items: center; justify-content: center;
  }
  .card-back .brand { color: var(--white); font-size: 29px; }
  .card-back .brand-mark { width: 32px; height: 32px; }
</style>
</head>
<body>
  <section class="card card-front" aria-label="Business card front">
    <div class="brand"><span class="brand-mark"></span>Tallowmere Capital Partners</div>
    <div class="person">
      <p class="person-name">Dorian Vale</p>
      <p class="person-title">Director</p>
    </div>
    <span class="divider"></span>
    <ul class="contacts">
      <li><svg viewBox="0 0 12 12" aria-hidden="true"><path d="M1 4c0-2 2-3 5-3s5 1 5 3l-2 1-1-1.5H4L3 5zM3 6h6l1 5H2z"/></svg>(555) 271-6094</li>
      <li><svg viewBox="0 0 12 12" aria-hidden="true"><path d="M0 2h12v8H0zM1 3l5 4 5-4"/></svg>rpoulsen@tallowmerecap.example</li>
      <li><svg viewBox="0 0 12 12" aria-hidden="true"><circle cx="6" cy="6" r="5.5"/></svg>www.tallowmerecap.example</li>
    </ul>
    <div class="address-band">24836 Orchard Ave. Suite 400, CA 93518</div>
  </section>

  <section class="card card-back" aria-label="Business card back">
    <div class="brand"><span class="brand-mark"></span>Tallowmere Capital Partners</div>
  </section>
</body>
</html>
```